label update for bottle change

The goal is to adapt the label's design and shape to the new bottle, maintaining its defining elements such as the font, vertical name, company logo, background pattern, and color. The new design should not be identical to the old one, but rather an evolution of it. The gold stripe on the bottom is not mandatory, but the writing "BASSANO DEL GRAPPA / EST. 1886" must be retained, slightly enlarged.

The font name is: Brandon Text

```html
<!DOCTYPE html>
<html lang="it">
<head>
<meta charset="utf-8">
<title>Amaro di Carattere Carciofo – etichetta</title>
<link rel="stylesheet" href="https://fonts.googleapis.com/css2?family=Libre+Caslon+Text:wght@400;700&family=Montserrat:wght@400;500;600;700&display=swap">
<style>
  :root {
    --bg: #efece6;
    --purple: #3e2a5e;
    --gold: #b08a4a;
    --gold-band: #9a7a45;
    --gold-text: #c9a35c;
    --cream: #f4efe4;
    --muted: #9c8fb3;
  }
  * { margin: 0; padding: 0; box-sizing: border-box; }
  html, body { width: 900px; height: 1200px; overflow: hidden; background: var(--bg); }
  .canvas { position: relative; width: 900px; height: 1200px; }

  .label {
    position: absolute; left: 60px; top: 110px; width: 780px; height: 980px;
    background: var(--purple);
    box-shadow: 0 6px 24px rgba(40, 25, 60, .18);
    overflow: hidden;
  }
  .rule-top {
    position: absolute; left: 40px; right: 40px; top: 30px; height: 2px; background: var(--gold);
  }
  .maker {
    position: absolute; left: 0; right: 0; top: 62px; text-align: center;
    font-family: 'Montserrat', sans-serif; color: var(--cream);
  }
  .maker-kind {
    font-size: 11px; letter-spacing: .06em; color: var(--gold-text); font-weight: 500;
    margin-right: 8px; vertical-align: middle;
  }
  .maker-name {
    font-size: 32px; font-weight: 700; letter-spacing: .02em; vertical-align: middle;
  }

  .illustration {
    position: absolute; left: 125px; top: 130px; width: 430px; height: 650px;
  }

  .product {
    position: absolute; left: 45px; top: 640px; font-family: 'Libre Caslon Text', serif; color: var(--cream);
  }
  .product-kicker { font-size: 19px; letter-spacing: .06em; }
  .product-name { font-size: 62px; line-height: 1.05; letter-spacing: .01em; }

  .vertical-name {
    position: absolute; left: 630px; top: 785px;
    transform: rotate(-90deg); transform-origin: left top;
    font-family: 'Libre Caslon Text', serif; font-weight: 700;
    font-size: 92px; letter-spacing: .1em; color: var(--gold-text); white-space: nowrap;
    line-height: 1;
  }

  .side-text {
    position: absolute; top: 170px; width: 50px;
    font-family: 'Montserrat', sans-serif; font-size: 6px; line-height: 1.7; color: var(--muted);
  }
  .side-text.left { left: 10px; }
  .side-text.right { right: 6px; top: 140px; width: 42px; }
  .side-text p { margin-bottom: 26px; }

  .origin-band {
    position: absolute; left: 0; right: 0; bottom: 0; height: 177px; background: var(--gold-band);
    text-align: center; color: var(--cream); font-family: 'Montserrat', sans-serif;
  }
  .origin-place { margin-top: 46px; font-size: 38px; font-weight: 600; letter-spacing: .04em; }
  .origin-est {
    margin-top: 16px; display: flex; align-items: center; justify-content: center; gap: 18px;
    font-size: 20px; font-weight: 500; letter-spacing: .14em;
  }
  .origin-est .line { width: 200px; height: 2px; background: var(--cream); }
</style>
</head>
<body>
<div class="canvas">
  <section class="label">
    <div class="rule-top"></div>

    <header class="maker">
      <span class="maker-kind">FABBRICA LIQUORI</span>
      <span class="maker-name">F.LLI MARCHETTI,</span>
    </header>

    <div class="side-text left">
      <p>Infuso di erbe amare</p>
      <p>e carciofo selezionato</p>
      <p>Prodotto in Italia</p>
    </div>

    <div class="side-text right">
      <p>Servire fresco</p>
      <p>con ghiaccio</p>
      <p>Alc. 28% vol</p>
      <p>Contenuto 70 cl</p>
    </div>

    <svg class="illustration" viewBox="0 0 430 650" role="img" aria-label="Illustrazione di un carciofo con stelo, foglie verdi e dorate sfumate di rosso">
      <defs>
        <radialGradient id="artichokeTone" cx="45%" cy="38%" r="60%">
          <stop offset="0%" stop-color="#b9734a"/>
          <stop offset="55%" stop-color="#a89a55"/>
          <stop offset="100%" stop-color="#7fa25a" stop-opacity="0"/>
        </radialGradient>
      </defs>
      <rect width="430" height="650" fill="url(#artichokeTone)"/>
    </svg>

    <div class="product">
      <div class="product-kicker">AMARO DI CARATTERE</div>
      <div class="product-name">CARCIOFO</div>
    </div>

    <div class="vertical-name">CARCIOFO</div>

    <footer class="origin-band">
      <div class="origin-place">BASSANO DEL GRAPPA</div>
      <div class="origin-est"><span class="line"></span><span>/ EST. 1886</span><span class="line"></span></div>
    </footer>
  </section>
</div>
</body>
</html>
```